* see below *
Project: Stationary for Law Firm
Stationary for Law Firm - Law
Stationary for Law Firm
Use standard fonts
Dorian Valesko, Esq.
Managing Partner
4382 Linden Terrace Brooklyn, New York 11356
dorian@valeskolegal.com
www.ValeskoLegal.com
This is a design for a stationary, not for a business card.
DorianValesko DorianValesko
This is a design for a stationary, not for a business card. I need a design for a letterhead stationary

```html
<!DOCTYPE html>
<html lang="en">
<head>
<meta charset="utf-8">
<title>Dorian Valesko, LLP — Stationery</title>
<link href="https://fonts.googleapis.com/css2?family=Cinzel:wght@500&family=Open+Sans:ital,wght@0,400;0,600;1,400&display=swap" rel="stylesheet">
<style>
  :root{
    --bg:#ebebeb;
    --paper:#ffffff;
    --maroon:#7b1a22;
    --gray:#6e6e6e;
    --ink:#4a4a4a;
    --light:#f4f4f4;
  }
  *{box-sizing:border-box;margin:0;padding:0}
  html,body{width:1200px;height:936px;overflow:hidden;background:var(--bg)}
  body{position:relative;font-family:"Open Sans",Arial,sans-serif;color:var(--ink)}
  .piece{position:absolute;background:var(--paper);overflow:hidden;box-shadow:0 1px 3px rgba(0,0,0,.12)}
  .wave{position:absolute;left:0;bottom:0;width:100%;display:block}

  .brand{display:flex;flex-direction:column;align-items:center;text-align:center}
  .brand-row{display:flex;align-items:center;gap:6px}
  .brand-mark{background:var(--maroon);flex:none}
  .brand-name{font-family:"Cinzel",Georgia,serif;font-weight:500;color:var(--maroon);white-space:nowrap}
  .brand-tag{display:flex;align-items:center;gap:6px;color:var(--gray);font-family:"Cinzel",Georgia,serif;letter-spacing:.18em;white-space:nowrap}
  .brand-tag::before,.brand-tag::after{content:"";height:1px;background:var(--gray);flex:1;min-width:12px}

  /* Letterhead */
  .letterhead{left:178px;top:51px;width:400px;height:610px}
  .letterhead .brand{position:absolute;left:30px;top:30px;align-items:flex-start}
  .letterhead .brand-mark{width:18px;height:18px}
  .letterhead .brand-name{font-size:12px}
  .letterhead .brand-tag{font-size:5.5px;width:140px}
  .letter-body{position:absolute;left:30px;top:110px;width:300px;font-size:5.6px;line-height:1.6}
  .letter-body p{margin-bottom:9px}
  .letter-body .sign-space{height:22px}
  .letterhead .wave{height:220px}
  .letter-contact{position:absolute;right:34px;bottom:62px;color:#fff;font-size:5.6px;line-height:1.75;text-align:left;width:130px}

  /* Folder */
  .folder{left:634px;top:46px;width:432px;height:576px}
  .folder .brand{position:absolute;left:0;right:0;top:200px}
  .folder .brand-mark{width:44px;height:44px;margin-bottom:14px}
  .folder .brand-name{font-size:21px}
  .folder .brand-tag{font-size:8px;width:220px;margin-top:4px}
  .folder .wave{height:210px}
  .folder-web{position:absolute;left:0;right:0;bottom:56px;text-align:center;color:#fff;font-size:10px;letter-spacing:.18em}

  /* Business cards */
  .card{width:198px}
  .card-front{left:43px;top:655px;height:132px}
  .card-back{left:43px;top:796px;height:104px}
  .card .brand{position:absolute;left:16px;top:16px;align-items:flex-start}
  .card .brand-mark{width:11px;height:11px}
  .card .brand-name{font-size:8px}
  .card .brand-tag{font-size:3.6px;width:90px}
  .card-front .wave{height:70px}
  .card-info{position:absolute;right:12px;top:14px;text-align:right;font-size:4.6px;line-height:1.7;color:var(--ink)}
  .card-info strong{color:var(--maroon);font-weight:600;font-size:5.4px}
  .card-back .brand{left:0;right:0;top:36px;align-items:center}
  .card-back .brand-mark{width:14px;height:14px}
  .card-back .brand-name{font-size:10px}
  .card-back .brand-tag{font-size:4.2px;width:110px}

  /* Envelope front */
  .envelope{left:266px;top:665px;width:457px;height:228px}
  .envelope .brand{position:absolute;left:24px;top:22px;align-items:flex-start}
  .envelope .brand-mark{width:16px;height:16px}
  .envelope .brand-name{font-size:11px}
  .envelope .brand-tag{font-size:5px;width:130px}
  .envelope-return{position:absolute;left:24px;top:76px;font-size:5.4px;line-height:1.6}
  .envelope .wave{height:118px}
  .envelope-web{position:absolute;left:0;right:0;bottom:14px;text-align:center;color:#fff;font-size:7px;letter-spacing:.16em}

  /* Envelope back */
  .envelope-back{left:736px;top:672px;width:431px;height:216px;background:var(--maroon)}
  .envelope-back svg{position:absolute;left:0;top:0;width:100%;height:100%}
  .envelope-back-web{position:absolute;left:0;right:0;bottom:66px;text-align:center;color:#fff;font-size:9px;letter-spacing:.18em}
</style>
</head>
<body>

<svg width="0" height="0" style="position:absolute" aria-hidden="true">
  <symbol id="wave-band" viewBox="0 0 400 220" preserveAspectRatio="none">
    <path d="M0,62 C110,-8 260,-10 400,22 L400,34 C260,6 120,10 0,78Z" fill="#7a7a7a"/>
    <path d="M0,82 C120,16 260,12 400,40 L400,48 C260,22 120,28 0,92Z" fill="#9a9a9a"/>
    <path d="M0,98 C130,34 270,26 400,56 L400,220 L0,220Z" fill="#7b1a22"/>
    <path d="M0,70 C115,4 262,0 400,29" fill="none" stroke="#ffffff" stroke-width="1.2"/>
  </symbol>
</svg>

<!-- Letterhead -->
<section class="piece letterhead">
  <div class="brand">
    <div class="brand-row"><span class="brand-mark"></span><span class="brand-name">Dorian Valesko, LLP</span></div>
    <span class="brand-tag">Attorneys at Law</span>
  </div>
  <div class="letter-body">
    <p>July 2, 2024<br>Client Name<br>RE: Engagement Letter</p>
    <p>We write to confirm the terms of our engagement and the scope of legal services to be provided by our firm in the matter described above. Please review the enclosed documents carefully.</p>
    <p>Our team will keep you informed of every development and respond promptly to your questions. Do not hesitate to contact our office at any time.</p>
    <p>Thank you for placing your trust in our firm. We look forward to working with you toward a favorable and timely resolution of this matter.</p>
    <p>Best Regards,</p>
    <div class="sign-space"></div>
    <p>Dorian Valesko, Esq.<br>Managing Partner</p>
  </div>
  <svg class="wave"><use href="#wave-band" width="100%" height="100%"/></svg>
  <div class="letter-contact">
    4382 Linden Terrace<br>Brooklyn, New York 11356<br>T: (718) 555-0142<br>F: (718) 555-0143<br>dorian@valeskolegal.com<br>www.ValeskoLegal.com
  </div>
</section>

<!-- Presentation folder -->
<section class="piece folder">
  <div class="brand">
    <span class="brand-mark"></span>
    <span class="brand-name">Dorian Valesko, LLP</span>
    <span class="brand-tag">Attorneys at Law</span>
  </div>
  <svg class="wave"><use href="#wave-band" width="100%" height="100%"/></svg>
  <div class="folder-web">www.ValeskoLegal.com</div>
</section>

<!-- Business card front -->
<section class="piece card card-front">
  <div class="brand">
    <div class="brand-row"><span class="brand-mark"></span><span class="brand-name">Dorian Valesko</span></div>
    <span class="brand-tag">Attorneys at Law</span>
  </div>
  <div class="card-info">
    <strong>Dorian Valesko, Esq.</strong><br>Managing Partner<br>(718) 555-0142<br>dorian@valeskolegal.com
  </div>
  <svg class="wave"><use href="#wave-band" width="100%" height="100%"/></svg>
</section>

<!-- Business card back -->
<section class="piece card card-back">
  <div class="brand">
    <div class="brand-row"><span class="brand-mark"></span><span class="brand-name">Dorian Valesko, LLP</span></div>
    <span class="brand-tag">Attorneys at Law</span>
  </div>
</section>

<!-- Envelope front -->
<section class="piece envelope">
  <div class="brand">
    <div class="brand-row"><span class="brand-mark"></span><span class="brand-name">Dorian Valesko, LLP</span></div>
    <span class="brand-tag">Attorneys at Law</span>
  </div>
  <div class="envelope-return">4382 Linden Terrace<br>Brooklyn, New York 11356</div>
  <svg class="wave"><use href="#wave-band" width="100%" height="100%"/></svg>
  <div class="envelope-web">www.ValeskoLegal.com</div>
</section>

<!-- Envelope back -->
<section class="piece envelope-back">
  <svg viewBox="0 0 431 216" preserveAspectRatio="none">
    <polygon points="0,0 431,0 431,14 215,118 0,14" fill="#ffffff"/>
  </svg>
  <div class="envelope-back-web">www.ValeskoLegal.com</div>
</section>

</body>
</html>
```